VELT FLYER

WE SEND THIS AND OTHER FLYERS OUT TO OUR CUSTOMERS VIA EMAIL
WHAT WE AR AFTER IS A REVAMP/REDESIGN FOR OUR WEB FLYER TO STAND OUT BETTER AND TO FIT ONE 1 PAGE

```html
<!DOCTYPE html>
<html lang="en">
<head>
<meta charset="utf-8">
<title>VELT Automotive Cables Flyer</title>
<link rel="stylesheet" href="https://fonts.googleapis.com/css2?family=Nunito:wght@400;600;700;800;900&display=swap">
<style>
  :root {
    --frame: #444444;
    --paper: #ffffff;
    --yellow: #fff200;
    --ink: #231f20;
    --grey: #8a8a8a;
    --photo-light: #f7f7f7;
    --photo-dark: #dcdcdc;
  }
  * { margin: 0; padding: 0; box-sizing: border-box; }
  html, body { width: 927px; height: 1200px; overflow: hidden; }
  body { background: var(--frame); font-family: "Nunito", sans-serif; color: var(--ink); position: relative; }

  .flyer { position: absolute; left: 60px; top: 80px; width: 806px; height: 1041px; background: var(--yellow); overflow: hidden; }
  .flyer-shapes { position: absolute; inset: 0; width: 806px; height: 1041px; }

  .title { position: absolute; top: 12px; left: 0; width: 100%; text-align: center; font-weight: 900; font-size: 98px; line-height: 1; letter-spacing: 1px; }
  .subtitle { position: absolute; top: 110px; left: 0; width: 100%; text-align: center; font-weight: 800; font-size: 44px; line-height: 1; }

  .banner { position: absolute; top: 621px; left: 102px; width: 602px; height: 37px; }
  .banner svg { position: absolute; inset: 0; }
  .banner-text { position: relative; text-align: center; font-weight: 900; font-size: 29px; line-height: 37px; color: var(--yellow); letter-spacing: 0.3px; }

  .range { position: absolute; left: 0; width: 100%; text-align: center; font-size: 20px; line-height: 1; }
  .range.types { top: 677px; font-weight: 400; }
  .range.uses { top: 710px; font-weight: 600; text-transform: uppercase; }
  .range.uses-2 { top: 743px; font-weight: 600; text-transform: uppercase; }

  .quote { position: absolute; top: 783px; left: 0; width: 100%; text-align: center; font-weight: 900; font-size: 24px; line-height: 32px; }
  .quote-mark { position: absolute; font-weight: 900; font-size: 90px; line-height: 1; color: var(--grey); }
  .quote-mark.open { top: 765px; left: 140px; }
  .quote-mark.close { top: 838px; left: 600px; }

  .footer { position: absolute; left: 0; top: 907px; width: 100%; height: 118px; color: #ffffff; }
  .brand { position: absolute; left: 48px; top: 8px; font-weight: 800; font-size: 40px; line-height: 1; color: var(--yellow); letter-spacing: 0.5px; }
  .tagline { position: absolute; left: 80px; top: 55px; font-weight: 400; font-size: 23px; line-height: 1; letter-spacing: 0.5px; }
  .web-line { position: absolute; left: 60px; top: 94px; font-size: 12px; line-height: 14px; display: flex; align-items: center; gap: 8px; }
  .web-line .sep { color: var(--yellow); font-weight: 800; margin: 0 10px; }
  .contacts { position: absolute; left: 540px; top: 12px; list-style: none; }
  .contacts li { display: flex; align-items: center; gap: 16px; height: 25.5px; font-size: 15px; }
  .icon { width: 12px; height: 12px; flex: none; }
</style>
</head>
<body>
  <main class="flyer">
    <svg class="flyer-shapes" viewBox="0 0 806 1041" aria-hidden="true">
      <defs>
        <linearGradient id="photoTone" x1="0" y1="0" x2="0" y2="1">
          <stop offset="0" stop-color="var(--photo-light)"/>
          <stop offset="1" stop-color="var(--photo-dark)"/>
        </linearGradient>
      </defs>
      <path d="M0,0 H806 V300 Q403,860 0,300 Z" fill="var(--paper)"/>
      <path d="M0,300 Q403,850 806,300" fill="none" stroke="#c9c9c9" stroke-width="10"/>
      <path d="M0,305 Q403,870 806,305" fill="none" stroke="var(--ink)" stroke-width="9"/>
      <rect x="0" y="909" width="806" height="117" fill="var(--ink)"/>
      <rect x="0" y="1028" width="806" height="11" fill="var(--yellow)"/>
      <rect x="0" y="898" width="806" height="2" fill="var(--paper)" opacity="0.7"/>
    </svg>

    <svg class="flyer-shapes" viewBox="0 0 806 1041" role="img" aria-label="Product photo of assorted control cables with pull knobs, T-handles, threaded ends and ferrules">
      <path d="M40,145 H766 V330 Q403,790 40,330 Z" fill="url(#photoTone)" opacity="0.7"/>
    </svg>

    <h1 class="title">VELT</h1>
    <p class="subtitle">Automotive Cables</p>

    <div class="banner">
      <svg viewBox="0 0 602 37" preserveAspectRatio="none" aria-hidden="true"><polygon points="18,0 602,0 584,37 0,37" fill="var(--ink)"/></svg>
      <h2 class="banner-text">CABLES FOR ALL TYPES OF VEHICLES</h2>
    </div>

    <p class="range types">✸ Pull Type Cable ✸ Speedo - Tacho Cables ✸ Cordmaster Push ✸ Pull Cables</p>
    <p class="range uses">For &nbsp;✦ Accelerator ✦ Choke &nbsp;✦ Handbrake Speedo</p>
    <p class="range uses-2">✦ Gear Shift ✦ PTO etc.</p>

    <span class="quote-mark open" aria-hidden="true">“</span>
    <blockquote class="quote">&nbsp;&nbsp;&nbsp;Our aim is to have your parts repaired<br>with the quickest<br>turn-around times possible&nbsp;&nbsp;&nbsp;&nbsp;&nbsp;</blockquote>
    <span class="quote-mark close" aria-hidden="true">”</span>

    <footer class="footer">
      <p class="brand">VELT AUTO CENTRE</p>
      <p class="tagline">The Brake and Cable Specialists</p>
      <p class="web-line">
        <svg class="icon" viewBox="0 0 12 12" aria-hidden="true"><rect x="1" y="3" width="10" height="7" fill="var(--yellow)"/><path d="M1,3 L6,7 L11,3" fill="none" stroke="var(--ink)" stroke-width="1"/></svg>
        <span>parts@veltautocentre.co.nz</span>
        <span class="sep">|</span>
        <svg class="icon" viewBox="0 0 12 12" aria-hidden="true"><circle cx="6" cy="6" r="5" fill="var(--yellow)"/><path d="M1,6 H11 M6,1 V11 M6,1 Q2,6 6,11 M6,1 Q10,6 6,11" fill="none" stroke="var(--ink)" stroke-width="0.7"/></svg>
        <span>www.veltautocentre.co.nz</span>
      </p>
      <ul class="contacts">
        <li><svg class="icon" viewBox="0 0 12 12" aria-hidden="true"><path d="M6,11 C3,7 2,5.5 2,4.5 A4,4 0 0 1 10,4.5 C10,5.5 9,7 6,11 Z" fill="var(--yellow)"/><circle cx="6" cy="4.5" r="1.5" fill="var(--ink)"/></svg>42 Marlow Road Hamilton</li>
        <li><svg class="icon" viewBox="0 0 12 12" aria-hidden="true"><circle cx="5" cy="4" r="2.3" fill="var(--yellow)"/><path d="M1,11 Q5,5 9,11 Z" fill="var(--yellow)"/></svg>0800 55 01 82</li>
        <li><svg class="icon" viewBox="0 0 12 12" aria-hidden="true"><path d="M2,1.5 L4.3,1.5 L5,4 L3.8,5 Q5,7.5 7,8.2 L8,7 L10.5,7.7 L10.5,10 Q5,11 2,4 Z" fill="var(--yellow)"/></svg>07 555 0142</li>
        <li><svg class="icon" viewBox="0 0 12 12" aria-hidden="true"><rect x="3" y="1" width="6" height="3" fill="var(--yellow)"/><rect x="1" y="4.5" width="10" height="4.5" rx="1" fill="var(--yellow)"/><rect x="3" y="8" width="6" height="3" fill="var(--yellow)" stroke="var(--ink)" stroke-width="0.6"/></svg>07 555 0143</li>
      </ul>
    </footer>
  </main>
</body>
</html>
```